Email footer project

We are looking for a standardised email footer that can be changed monthly for various project we are working on.
Please refer to EMAIL FOOTER BRIEF FOR ALL INFORMATION

We have uploaded some previous footers as a sample.

Target Market(s)

property, environmental

Industry/Entity Type

energy and property

Colors
00AB8E
00BBA5
67D7C9
C6EFE9
E9F9F6

Requirements
Must have
• company branding - leafmarker.co.uk.

```html
<!DOCTYPE html>
<html lang="en">
<head>
<meta charset="utf-8">
<title>Leafmarker – Delivering Net Zero email footers</title>
<link rel="stylesheet" href="https://fonts.googleapis.com/css2?family=Quicksand:wght@500;600;700&family=Source+Sans+3:wght@400&display=swap">
<style>
  :root {
    --page: #ffffff;
    --label: #231f20;
    --mist: #e9f9f6;
    --foam: #c6efe9;
    --aqua: #67d7c9;
    --lagoon: #00bba5;
    --teal: #00ab8e;
    --deep-teal: #00745f;
    --title-teal: #006654;
    --white: #ffffff;
    --ink: #0f2a26;
  }
  * { margin: 0; padding: 0; box-sizing: border-box; }
  html, body { width: 1200px; height: 1000px; overflow: hidden; background: var(--page); }
  .sheet { position: relative; width: 1200px; height: 1000px; }

  .month-label {
    position: absolute; left: 100px;
    font-family: "Source Sans 3", sans-serif; font-weight: 400;
    font-size: 25px; color: var(--label); line-height: 1;
  }

  .footer-banner { position: absolute; left: 100px; width: 1000px; height: 125px; }
  .footer-banner svg.banner-shapes { position: absolute; inset: 0; width: 100%; height: 100%; }

  .banner-title {
    position: absolute; left: 51px; top: 16px;
    font-family: "Quicksand", sans-serif; font-weight: 700;
    font-size: 41px; line-height: 46px; letter-spacing: 1px;
    color: var(--title-teal);
  }

  .banner-message {
    position: absolute; left: 373px;
    font-family: "Quicksand", sans-serif; font-weight: 600;
    color: var(--white);
  }
  .message-small { top: 30px; font-size: 17px; line-height: 21px; letter-spacing: .3px; }
  .message-large { left: 403px; top: 28px; font-size: 26px; line-height: 34px; letter-spacing: .5px; }
  .message-medium { top: 22px; font-size: 20px; line-height: 26px; letter-spacing: .4px; }

  .cta-button {
    position: absolute; left: 776px; top: 30px; width: 180px; height: 52px;
    border-radius: 12px; background: var(--white);
    display: flex; align-items: center; justify-content: center;
    font-family: "Quicksand", sans-serif; font-weight: 700;
    font-size: 16.5px; letter-spacing: 1px; color: var(--ink);
    text-decoration: none;
  }
  .brand-address {
    position: absolute; left: 776px; top: 92px; width: 180px;
    text-align: center;
    font-family: "Quicksand", sans-serif; font-weight: 600;
    font-size: 13px; letter-spacing: .5px; color: var(--white);
  }
</style>
</head>
<body>
<main class="sheet">

  <svg width="0" height="0" style="position:absolute" aria-hidden="true">
    <defs>
      <radialGradient id="globe-glow" cx="0.78" cy="0.55" r="0.35">
        <stop offset="0" stop-color="#1f9a84"/>
        <stop offset="0.7" stop-color="#0b836d"/>
        <stop offset="1" stop-color="#00745f"/>
      </radialGradient>
    </defs>
  </svg>

  <p class="month-label" style="top:117px">March 2022</p>
  <section class="footer-banner" style="top:160px">
    <svg class="banner-shapes" viewBox="0 0 1000 125" preserveAspectRatio="none">
      <rect width="1000" height="125" fill="var(--lagoon)"/>
      <polygon points="317,0 713,0 735,66 715,125 320,125 340,66" fill="url(#globe-glow)" role="img" aria-label="Faded globe photograph behind the message"/>
      <polygon points="0,0 317,0 340,66 320,125 0,125" fill="var(--foam)"/>
    </svg>
    <h2 class="banner-title">DELIVERING<br>NET ZERO</h2>
    <p class="banner-message message-small">Leafmarker are running a webinar<br>as part of our webinar series on<br>MEES, EPCs and ESG</p>
    <a class="cta-button" href="#">REGISTER NOW</a>
    <p class="brand-address">leafmarker.co.uk</p>
  </section>

  <p class="month-label" style="top:320px">April 2022</p>
  <section class="footer-banner" style="top:363px">
    <svg class="banner-shapes" viewBox="0 0 1000 125" preserveAspectRatio="none">
      <rect width="1000" height="125" fill="var(--lagoon)"/>
      <polygon points="317,0 713,0 735,66 715,125 320,125 340,66" fill="url(#globe-glow)" role="img" aria-label="Faded globe photograph behind the message"/>
      <polygon points="0,0 317,0 340,66 320,125 0,125" fill="var(--foam)"/>
    </svg>
    <h2 class="banner-title">DELIVERING<br>NET ZERO</h2>
    <p class="banner-message message-large">Are you ready for<br>EPC changes?</p>
    <a class="cta-button" href="#">LEARN MORE</a>
    <p class="brand-address">leafmarker.co.uk</p>
  </section>

  <p class="month-label" style="top:515px">May 2022</p>
  <section class="footer-banner" style="top:554px">
    <svg class="banner-shapes" viewBox="0 0 1000 125" preserveAspectRatio="none">
      <rect width="1000" height="125" fill="var(--lagoon)"/>
      <polygon points="317,0 713,0 735,66 715,125 320,125 340,66" fill="url(#globe-glow)" role="img" aria-label="Faded globe photograph behind the message"/>
      <polygon points="0,0 317,0 340,66 320,125 0,125" fill="var(--foam)"/>
    </svg>
    <h2 class="banner-title">DELIVERING<br>NET ZERO</h2>
    <p class="banner-message message-medium">Leafmarker have a maturity<br>model to map out your<br>EPC Compliance.</p>
    <a class="cta-button" href="#">LEARN MORE</a>
    <p class="brand-address">leafmarker.co.uk</p>
  </section>

  <p class="month-label" style="top:720px">June 2022</p>
  <section class="footer-banner" style="top:762px">
    <svg class="banner-shapes" viewBox="0 0 1000 125" preserveAspectRatio="none">
      <rect width="1000" height="125" fill="var(--lagoon)"/>
      <polygon points="317,0 713,0 735,66 715,125 320,125 340,66" fill="url(#globe-glow)" role="img" aria-label="Faded globe photograph behind the message"/>
      <polygon points="0,0 317,0 340,66 320,125 0,125" fill="var(--foam)"/>
    </svg>
    <h2 class="banner-title">DELIVERING<br>NET ZERO</h2>
    <p class="banner-message message-medium">Leafmarker are launching<br>phase 2 of our Digital EPC<br>analylsis platform</p>
    <a class="cta-button" href="#">LEARN MORE</a>
    <p class="brand-address">leafmarker.co.uk</p>
  </section>

</main>
</body>
</html>
```